A4 onepager targeted to retailers selling vaping products

We're a startup with the capital and contacts to support our ambition to become the main manufacturer / distributor of e-liquids and vaping materials in the Belgium and The Netherlands.

We're looking for a one-pager in A4 format to sell our concept to professional retailers.

We should be able to import the template in MS Word so that we can alter or translate the text ourselves.

Blue Finch Mists refers to the Gullwing Sea Route, the ocean passenger line founded in 1871 and operating until 1937. Therefore we would like to print to have a somewhat art deco style.

We have made a board on pinterest that attempts to capture the feeling of the age. This is just meant as an inspiration, we're not looking to be close to something that is on thus board. The link: https://nl.pinboardly.example/jorvanleek/mist/

Thanks for reading through this, we're very much looking forward to your designs.

Target Market(s)

Professional retailers

Industry/Entity Type

Distributor

Font styles to use
Serif
Sans Serif

Requirements
Must have
• - Our logo
• - Professional
• - Art deco style, capturing the look and feel of: https://nl.pinboardly.example/jorvanleek/mist/
• Shoud include the following text:
• *** Blue Finch Mists is committed to bringing premium eCigarettes and eLiquids tot the mainstream consumer (smoker) by means of a comprehensive, transparent and easy to understand product range, competitive pricing and a convenient buying experience through reliable retail channels.
• Why should you retail eLiquids?
• - Exponentially growing market
• - eSmoking carries only a fraction of the health risks of smoking classic cigarettes.
• - Changing market: sale through the internet is forbidden as from 20/01/2017.
• - The (ex-) smokers prefer buying their nicotine products through the convenience of the retailers they know
• - The eCigarette will take market share away from regular cigarettes. Jumping on the bandwagon will assure that this will not negatively impact your sales figures
• - No excise tax on eLiquids leaves room for a better profit margin.
• Why should you work with Blue Finch Mists?
• - Know-how of the market and the industry.
• - Our products are 100% compliant with the new Belgian regulation
• - We only carry Premium Brands, all of them made in Europe and in ISO-certified laboratories and of course all of them have an excellent and distinctive taste.
• - We limit our offer to a very comprehensive and easy to understand product range, appealing to a very broad audience.
• - Competitive pricing policy ensuring a good retail profit margin
• - Quick delivery times
• - We son’t sell tot he consumer and are purely focused on selecting premium brand and helping our partners to market them in the best way possible.***
Nice to have
• - Would be nice to have a small reference to the late 1800, early 1900 ocean liners (marivella, etc...). This should not be too prominent
• - Would be nice to have a small reference to vaping or smoke. This should not be too prominent

```html
<!DOCTYPE html>
<html lang="en">
<head>
<meta charset="utf-8">
<title>Blue Finch Mists – Retailer One-Pager</title>
<link rel="stylesheet" href="https://fonts.googleapis.com/css2?family=Kurale&display=swap">
<style>
  :root {
    --stage: #ddd28b;
    --ink-font: "Kurale", Georgia, serif;
  }
  * { box-sizing: border-box; margin: 0; padding: 0; }
  html, body { width: 1200px; height: 1200px; overflow: hidden; }
  body { background: var(--stage); position: relative; font-family: var(--ink-font); }

  .poster {
    --paper: #2b2a26;
    --frame: #c9a56a;
    --text: #e6d2a8;
    --band-text: #e6d2a8;
    --accent: #c8202a;
    --figure-dark: #161512;
    --figure-base: #9c8458;
    position: absolute;
    width: 738px; height: 1044px;
    background: var(--paper);
    color: var(--text);
    transform-origin: top left;
    overflow: hidden;
  }
  .poster--dark { left: 46px; top: 46px; border: 2px solid #1c1b18; }
  .poster--light {
    --paper: #fbeed6;
    --frame: #e38c5c;
    --text: #4a4036;
    --band-text: #4a4036;
    --figure-dark: #3a3733;
    --figure-base: #b7ab9a;
    left: 822px; top: 610px;
    transform: scale(0.4553);
  }

  .poster__frame { position: absolute; inset: 0; width: 738px; height: 1044px; }

  .brand { position: absolute; left: 0; right: 0; top: 92px; text-align: center; }
  .brand__mark { width: 52px; height: 52px; border-radius: 50%; background: var(--accent); margin: 0 auto 22px; }
  .brand__name { font-size: 32px; letter-spacing: 1px; color: var(--text); line-height: 1; }

  .intro {
    position: absolute; left: 60px; width: 618px; top: 262px;
    text-align: center; font-size: 14px; line-height: 17.6px; letter-spacing: 0.3px;
    white-space: nowrap;
  }

  .section-band {
    position: absolute; left: 48px; width: 330px; height: 20px;
    background: linear-gradient(90deg, var(--frame) 0%, color-mix(in srgb, var(--frame) 55%, transparent) 60%, transparent 100%);
    color: var(--band-text);
    font-size: 12.5px; font-weight: 400; line-height: 20px; padding-left: 26px; letter-spacing: 0.3px;
  }
  .section-band--retail { top: 362px; }
  .section-band--partner { top: 622px; }

  .benefits {
    position: absolute; left: 74px; list-style: none;
    font-size: 12.6px; line-height: 15.8px; letter-spacing: 0.3px;
    white-space: nowrap;
  }
  .benefits--retail { top: 386px; }
  .benefits--partner { top: 653px; }
  .benefits li { position: relative; padding-left: 24px; }
  .benefits li::before {
    content: ""; position: absolute; left: 5px; top: 6px;
    width: 10px; height: 3px; background: var(--text);
    clip-path: polygon(0 0, 70% 0, 100% 50%, 70% 100%, 0 100%, 20% 50%);
  }

  .figure-art {
    position: absolute; left: 495px; top: 400px; width: 200px; height: 450px;
    background:
      radial-gradient(ellipse 48% 4% at 50% 96%, var(--figure-base) 0 96%, transparent 100%),
      radial-gradient(ellipse 40% 46% at 50% 48%, var(--figure-dark) 0 70%, transparent 100%);
  }

  .contact { position: absolute; top: 895px; left: 0; right: 0; height: 70px; font-size: 13.4px; line-height: 17.4px; letter-spacing: 0.3px; }
  .contact__stamp {
    position: absolute; left: 84px; top: -6px; width: 80px; height: 80px;
    border-radius: 50%; background: var(--accent);
    border: 4px solid var(--frame);
  }
  .contact__address { position: absolute; left: 196px; font-style: normal; }
  .contact__company { text-decoration: underline; }
  .contact__lines { position: absolute; left: 385px; font-style: normal; }
</style>
</head>
<body>

<article class="poster poster--dark">
  <svg class="poster__frame" viewBox="0 0 738 1044" aria-hidden="true">
    <g fill="none" stroke="var(--frame)">
      <path d="M68 28 H670 L708 64 V980 L670 1016 H68 L30 980 V64 Z" stroke-width="2.5"/>
      <path d="M76 36 H662 L700 70 V974 L662 1008 H76 L38 974 V70 Z" stroke-width="1"/>
      <rect x="48" y="74" width="642" height="894" stroke-width="2.5"/>
      <line x1="48" y1="883" x2="690" y2="883" stroke-width="2.5"/>
      <line x1="70" y1="54" x2="272" y2="54" stroke-width="4" stroke-dasharray="3 4"/>
      <line x1="466" y1="54" x2="668" y2="54" stroke-width="4" stroke-dasharray="3 4"/>
      <line x1="70" y1="993" x2="272" y2="993" stroke-width="4" stroke-dasharray="3 4"/>
      <line x1="466" y1="993" x2="668" y2="993" stroke-width="4" stroke-dasharray="3 4"/>
      <line x1="272" y1="54" x2="466" y2="54" stroke-width="1.5"/>
      <line x1="272" y1="993" x2="466" y2="993" stroke-width="1.5"/>
      <circle cx="34" cy="35" r="8" stroke-width="4"/>
      <circle cx="704" cy="35" r="8" stroke-width="4"/>
      <circle cx="34" cy="1009" r="8" stroke-width="4"/>
      <circle cx="704" cy="1009" r="8" stroke-width="4"/>
    </g>
    <g fill="var(--frame)" opacity="0.75">
      <ellipse cx="338" cy="54" rx="26" ry="13" role="img" aria-label="Scroll ornament"/>
      <ellipse cx="400" cy="54" rx="26" ry="13" role="img" aria-label="Scroll ornament"/>
      <ellipse cx="338" cy="993" rx="26" ry="13" role="img" aria-label="Scroll ornament"/>
      <ellipse cx="400" cy="993" rx="26" ry="13" role="img" aria-label="Scroll ornament"/>
    </g>
  </svg>

  <header class="brand">
    <div class="brand__mark"></div>
    <div class="brand__name">Blue Finch Mists</div>
  </header>

  <p class="intro">Blue Finch Mists is committed to bringing premium eCigarettes and<br>eLiquids tot the mainstream consumer (smoker) by means of<br>a comprehensive, transparent and easy to understand product range,<br>competitive pricing and a convenient buying experience through<br>reliable retail channels.</p>

  <h2 class="section-band section-band--retail">Why should you retail eLiquids?</h2>
  <ul class="benefits benefits--retail">
    <li>Exponentially growing market</li>
    <li>eSmoking carries only a fraction of the health risks of<br>smoking classic cigarettes.</li>
    <li>Changing market: sale through the internet is<br>forbidden as from 20/01/2017.</li>
    <li>The (ex-) smokers prefer buying their nicotine products<br>through the convenience of<br>the retailers they know</li>
    <li>The eCigarette will take market share away from<br>regular cigarettes. Jumping on the bandwago will<br>assure that this will not negatively impact your sales<br>figures</li>
    <li>No excise tax on eLiquids leaves room for a better<br>profit margin.</li>
  </ul>

  <h2 class="section-band section-band--partner">Why should you work with Blue Finch Mists?</h2>
  <ul class="benefits benefits--partner">
    <li>Know-how of the market and the industry.</li>
    <li>Our products are 100% compliant with the new Belgian<br>regulation</li>
    <li>We only carry Premium Brands, all of them made in Europe<br>and in ISO-certified laboratories and of course all of them have<br>an excellent and distinctive taste.</li>
    <li>We limit our offer to a very comprehensive and easy to<br>understand product range, appealing to a very broad<br>audience.</li>
    <li>Competitive pricing policy ensuring a good retail profit margin</li>
    <li>Quick delivery times</li>
    <li>We don't sell to the consumer and are purely focused on<br>selecting premium brand and helping our partners to market<br>them in the best way possible.</li>
  </ul>

  <div class="figure-art" role="img" aria-label="Art deco silhouette of an elegant couple smoking, standing on a round base"></div>

  <footer class="contact">
    <div class="contact__stamp"></div>
    <address class="contact__address">
      <span class="contact__company">Harbourline Trading Co.</span><br>
      18 Quay Lane, #12<br>
      Portsville, Florida, 32199<br>
      United States of America
    </address>
    <address class="contact__lines">
      Phone : +1 55 01 23 45<br>
      Fax &nbsp;&nbsp;: +1 55 01 23 46<br>
      Email : hello@harbourline.example<br>
      Site : http://harbourline.example
    </address>
  </footer>
</article>

<article class="poster poster--light">
  <svg class="poster__frame" viewBox="0 0 738 1044" aria-hidden="true">
    <g fill="none" stroke="var(--frame)">
      <path d="M68 28 H670 L708 64 V980 L670 1016 H68 L30 980 V64 Z" stroke-width="2.5"/>
      <path d="M76 36 H662 L700 70 V974 L662 1008 H76 L38 974 V70 Z" stroke-width="1"/>
      <rect x="48" y="74" width="642" height="894" stroke-width="2.5"/>
      <line x1="48" y1="883" x2="690" y2="883" stroke-width="2.5"/>
      <line x1="70" y1="54" x2="272" y2="54" stroke-width="4" stroke-dasharray="3 4"/>
      <line x1="466" y1="54" x2="668" y2="54" stroke-width="4" stroke-dasharray="3 4"/>
      <line x1="70" y1="993" x2="272" y2="993" stroke-width="4" stroke-dasharray="3 4"/>
      <line x1="466" y1="993" x2="668" y2="993" stroke-width="4" stroke-dasharray="3 4"/>
      <line x1="272" y1="54" x2="466" y2="54" stroke-width="1.5"/>
      <line x1="272" y1="993" x2="466" y2="993" stroke-width="1.5"/>
      <circle cx="34" cy="35" r="8" stroke-width="4"/>
      <circle cx="704" cy="35" r="8" stroke-width="4"/>
      <circle cx="34" cy="1009" r="8" stroke-width="4"/>
      <circle cx="704" cy="1009" r="8" stroke-width="4"/>
    </g>
    <g fill="var(--frame)" opacity="0.75">
      <ellipse cx="338" cy="54" rx="26" ry="13" role="img" aria-label="Scroll ornament"/>
      <ellipse cx="400" cy="54" rx="26" ry="13" role="img" aria-label="Scroll ornament"/>
      <ellipse cx="338" cy="993" rx="26" ry="13" role="img" aria-label="Scroll ornament"/>
      <ellipse cx="400" cy="993" rx="26" ry="13" role="img" aria-label="Scroll ornament"/>
    </g>
  </svg>

  <header class="brand">
    <div class="brand__mark"></div>
    <div class="brand__name">Blue Finch Mists</div>
  </header>

  <p class="intro">Blue Finch Mists is committed to bringing premium eCigarettes and<br>eLiquids tot the mainstream consumer (smoker) by means of<br>a comprehensive, transparent and easy to understand product range,<br>competitive pricing and a convenient buying experience through<br>reliable retail channels.</p>

  <h2 class="section-band section-band--retail">Why should you retail eLiquids?</h2>
  <ul class="benefits benefits--retail">
    <li>Exponentially growing market</li>
    <li>eSmoking carries only a fraction of the health risks of<br>smoking classic cigarettes.</li>
    <li>Changing market: sale through the internet is<br>forbidden as from 20/01/2017.</li>
    <li>The (ex-) smokers prefer buying their nicotine products<br>through the convenience of<br>the retailers they know</li>
    <li>The eCigarette will take market share away from<br>regular cigarettes. Jumping on the bandwago will<br>assure that this will not negatively impact your sales<br>figures</li>
    <li>No excise tax on eLiquids leaves room for a better<br>profit margin.</li>
  </ul>

  <h2 class="section-band section-band--partner">Why should you work with Blue Finch Mists?</h2>
  <ul class="benefits benefits--partner">
    <li>Know-how of the market and the industry.</li>
    <li>Our products are 100% compliant with the new Belgian<br>regulation</li>
    <li>We only carry Premium Brands, all of them made in Europe<br>and in ISO-certified laboratories and of course all of them have<br>an excellent and distinctive taste.</li>
    <li>We limit our offer to a very comprehensive and easy to<br>understand product range, appealing to a very broad<br>audience.</li>
    <li>Competitive pricing policy ensuring a good retail profit margin</li>
    <li>Quick delivery times</li>
    <li>We don't sell to the consumer and are purely focused on<br>selecting premium brand and helping our partners to market<br>them in the best way possible.</li>
  </ul>

  <div class="figure-art" role="img" aria-label="Art deco silhouette of an elegant couple smoking, standing on a round base"></div>

  <footer class="contact">
    <div class="contact__stamp"></div>
    <address class="contact__address">
      <span class="contact__company">Harbourline Trading Co.</span><br>
      18 Quay Lane, #12<br>
      Portsville, Florida, 32199<br>
      United States of America
    </address>
    <address class="contact__lines">
      Phone : +1 55 01 23 45<br>
      Fax &nbsp;&nbsp;: +1 55 01 23 46<br>
      Email : hello@harbourline.example<br>
      Site : http://harbourline.example
    </address>
  </footer>
</article>

</body>
</html>
```